International Life/Work Balance and Personal Growth company needs a new business card

I have got the logo already and need a creative way in putting it together....

Target Market(s)

corporate - business for stress management/work/life balance seminars
anybody else who is interested in living a extraordinary life and is into Wellness and is open to changing habits

Industry/Entity Type

Business

Requirements
Must have
• must include my photo on the front

On the business card.... yes, both sides.... my name Marisol Pettark mobile 0476 581 904 www.dawnquill.com, also the facebook sign and marisol@dawnquill.com as email, also my pic see attachment and logo with slogan

Workplace Wellness Seminars
Stress Management
Law of Attraction w/s
Personal Transformations
Kestrel Yoga and Pilates

slogan: wellness ~ success ~ peace of mind
Nice to have
• I like the colors of the logo so that should match the card. I like flowing contemporary lines....something that has the feeling of peace and upliftment.

Font could be "chalkboard" or something similar....

```html
<!DOCTYPE html>
<html lang="en">
<head>
<meta charset="utf-8">
<title>Dawn Quill – Business Card</title>
<link href="https://fonts.googleapis.com/css2?family=Francois+One&family=Short+Stack&display=swap" rel="stylesheet">
<style>
  :root {
    --bg: #e4e4e4;
    --card: #ffffff;
    --brand-green: #3f7a2c;
    --lime: #9cc43a;
    --navy: #27306b;
    --blue: #1e63ad;
    --social: #3b5a9a;
    --photo-dark: #1c1714;
    --photo-warm: #c9683a;
  }
  * { box-sizing: border-box; margin: 0; padding: 0; }
  html, body { width: 1200px; height: 901px; overflow: hidden; background: var(--bg); }
  .canvas { position: relative; width: 1200px; height: 901px; }

  .card {
    position: absolute;
    width: 620px; height: 360px;
    background: var(--card);
    overflow: hidden;
    border: 1px solid #cfcfcf;
  }
  .card--front { left: 60px; top: 70px; }
  .card--back { left: 520px; top: 470px; }

  .brand { position: absolute; display: flex; align-items: center; gap: 10px; }
  .brand__dot { width: 44px; height: 44px; border-radius: 50%; background: var(--blue); }
  .brand__name {
    font-family: "Short Stack", cursive;
    color: var(--brand-green);
    font-size: 21px; line-height: 22px;
  }
  .card--front .brand { left: 42px; top: 60px; }
  .card--back .brand { left: 380px; top: 62px; }

  .holder-name {
    position: absolute; left: 50px; top: 146px;
    font-family: "Francois One", sans-serif;
    color: var(--brand-green);
    font-size: 44px; line-height: 1;
    white-space: nowrap;
  }
  .social-mark {
    position: absolute; left: 312px; top: 206px;
    width: 24px; height: 24px; background: var(--social);
  }
  .contacts {
    position: absolute; left: 52px; top: 206px;
    list-style: none;
    font-family: "Short Stack", cursive;
    color: var(--navy);
    font-size: 17px; line-height: 25px;
  }
  .portrait {
    position: absolute; left: 410px; top: -20px;
    width: 260px; height: 260px; border-radius: 50%;
    background: linear-gradient(180deg, var(--photo-dark) 0%, var(--photo-dark) 60%, var(--photo-warm) 100%);
  }
  .wave-band {
    position: absolute; left: 0; top: 300px;
    width: 620px; height: 22px;
    background: linear-gradient(90deg, #1d3f8f 0%, #1e8fd0 55%, var(--lime) 80%, var(--brand-green) 100%);
  }

  .services-panel { position: absolute; left: 0; top: 0; width: 360px; height: 360px; }
  .services {
    position: absolute; left: 0; top: 102px; width: 300px;
    list-style: none; text-align: center;
    font-family: "Short Stack", cursive;
    color: #ffffff; font-size: 16px; line-height: 25px;
  }
  .slogan {
    position: absolute; right: 34px; top: 172px;
    text-align: right;
    font-family: "Francois One", sans-serif;
    color: var(--navy);
    font-size: 34px; line-height: 42px;
  }
</style>
</head>
<body>
<main class="canvas">

  <section class="card card--front" aria-label="Card front">
    <div class="brand">
      <span class="brand__dot"></span>
      <span class="brand__name">Dawn<br>Quill</span>
    </div>

    <h1 class="holder-name">Marisol Pettark</h1>
    <span class="social-mark" aria-label="Social page"></span>
    <ul class="contacts">
      <li>0476 581 904</li>
      <li>www.dawnquill.com</li>
      <li>marisol@dawnquill.com</li>
    </ul>

    <div class="portrait" role="img" aria-label="Portrait photo of Marisol Pettark"></div>

    <div class="wave-band" role="img" aria-label="Flowing blue and green wave decoration"></div>
  </section>

  <section class="card card--back" aria-label="Card back">
    <svg class="services-panel" viewBox="0 0 360 360" aria-hidden="true">
      <path d="M0 46 H290 Q360 172 290 296 H0 Z" fill="var(--lime)"/>
    </svg>
    <ul class="services">
      <li>Workplace Wellness Seminars</li>
      <li>Stress Management</li>
      <li>Law of Attraction w/s</li>
      <li>Personal Transformations</li>
      <li>Kestrel Yoga and Pilates</li>
    </ul>

    <div class="brand">
      <span class="brand__dot"></span>
      <span class="brand__name">Dawn<br>Quill</span>
    </div>

    <p class="slogan">wellness<br>success<br>peace of mind</p>
  </section>

</main>
</body>
</html>
```